Banners for a bowtie/tie Fashion shop

I need banners (770x100) for a necktie and bowtie shop (http://www.movelia.dk)

5 BOWTIE BANNERS:

I need the 3 text versions for eatch bowtie banner:

Danmarks største udvalg af butterfly
Køb butterfly. FRI fragt og FRI retur
Butterfly fra 199,- inkl. FRI fragt

5 NECKTIE BANNERS:

I need the 3 text versions for eatch necktie banner:

Danmarks største udvalg af slips
Køb slips. FRI fragt og FRI retur
Slips fra 199,- inkl. FRI fragt

All banners should contain the logo. All in JPG format and Photoshop/Inddesign/illustrator format

Target Market(s)

Guys and Gays

Industry/Entity Type

Shop

Requirements
Must have
• Logo
Nice to have
• Nice new pictures

```html
<!DOCTYPE html>
<html lang="da">
<head>
<meta charset="utf-8">
<title>tivanko – butterfly banner</title>
<link rel="stylesheet" href="https://fonts.googleapis.com/css2?family=Open+Sans:wght@400;600&display=swap">
<style>
  :root {
    --navy: #1d2a57;
    --red: #b3323b;
    --white: #ffffff;
    --ink: #2a2a2a;
    --tie-navy-light: #2f3d72;
    --tie-check-red: #d9555a;
    --tie-check-blue: #5a78c0;
    --tie-check-light: #f3eef0;
  }
  * { box-sizing: border-box; margin: 0; padding: 0; }
  html, body { width: 1200px; height: 156px; overflow: hidden; background: var(--white); }
  .banner {
    position: relative;
    display: block;
    width: 1200px;
    height: 156px;
    background: var(--white);
    text-decoration: none;
    font-family: "Open Sans", Arial, sans-serif;
  }
  .headline { font-size: inherit; font-weight: inherit; }
  .headline-line {
    position: absolute;
    left: 0;
    display: flex;
    align-items: center;
    padding-left: 14px;
    color: var(--white);
    font-weight: 600;
    font-size: 33px;
    line-height: 1;
    white-space: nowrap;
  }
  .headline-line--top { top: 12px; height: 60px; width: 371px; background: var(--navy); }
  .headline-line--bottom { top: 83px; height: 59px; width: 402px; background: var(--red); }
  .product {
    position: absolute;
    border-radius: 40% / 30%;
  }
  .product--dotted-bowtie {
    left: 449px; top: 12px; width: 205px; height: 116px;
    background: radial-gradient(ellipse at center, var(--tie-navy-light), var(--navy));
  }
  .product--checked-bowtie {
    left: 787px; top: 10px; width: 238px; height: 126px;
    background: linear-gradient(135deg, var(--tie-check-red), var(--tie-check-light) 50%, var(--tie-check-blue));
  }
  .brand-name {
    position: absolute;
    left: 1042px;
    top: 100px;
    font-weight: 400;
    font-size: 36px;
    line-height: 1;
    color: var(--ink);
    letter-spacing: -0.5px;
    white-space: nowrap;
  }
</style>
</head>
<body>
  <a class="banner" href="http://www.tivanko.dk">
    <h1 class="headline">
      <span class="headline-line headline-line--top">Danmarks største</span>
      <span class="headline-line headline-line--bottom">udvalg af butterfly</span>
    </h1>
    <div class="product product--dotted-bowtie" role="img" aria-label="Photo of a navy bowtie with small white dots"></div>
    <div class="product product--checked-bowtie" role="img" aria-label="Photo of a red, blue and white checked bowtie"></div>
    <span class="brand-name">tivanko</span>
  </a>
</body>
</html>
```